Survey App for phone users trying a new phone with Dual connectivity

Survey App Brief<br/>Design For an Android Survey App for users' feedback on Call, SMS, Data and Streaming Experience on their Mobile phones.<br/><br/>Purpose of the App<br/>To ensure that the user's experience is not impacted by the network switching between two network on the special mobile phones they newly started using.<br/><br/>App Requirements:<br/>First screen: The registration screen, where the user needs to enter the following:<br/>Name: text box<br/>Phone Number: text box<br/>Group Number : <br/><br/>An information text:<br/>By Registering I agree to participate in the Survey.<br/><br/>Register: Button<br/><br/>Start Screen - Survey screens (next time user open the App this will be the first screen):<br/>We need feedback for 4 indicators:<br/>Call Experience<br/>SMS Experience<br/>Data Experience<br/>Streaming Experience<br/><br/>Each Experience can be in the form of a questionnaire or Satisfied/ Somewhat Satisfied / Extremely Satisfied form with radio buttons or on a scale of 1 to 5. We need to ensure that the format used is very professional.<br/><br/>An optional text box for the user to enter the comment in a free format.<br/><br/>This can be done in 4 different screens or in one single screen if it does not give a clumsy look.<br/><br/>A Send button at the end to submit the Survey.<br/><br/>We need a burger menu at the top left corner of this screen, which when expanded will provide 5 options:<br/>Edit User Profile<br/>Survey interval Timer<br/>FAQ<br/>Exit<br/>About<br/><br/><br/>Please ensure that the app is simple, friendly, lively and professional at the same time so that it ignites an interest in the user to use the app.<br/>Use Logo as appropriate.
Industry/Entity Type
Telecommunications
Colors
Designer to choose colors to be used in the design.
Look and feel
Each slider illustrates characteristics of the customer's brand and the style your logo design should communicate.

```html
<!DOCTYPE html>
<html lang="en">
<head>
<meta charset="utf-8">
<title>Survey App Screens</title>
<link href="https://fonts.googleapis.com/css2?family=Roboto:wght@300;400;500&display=swap" rel="stylesheet">
<style>
:root{
  --blue:#3aaee8;
  --blue-dark:#2a9ad6;
  --ink:#5a6470;
  --muted:#8a949c;
  --line:#e6e8ea;
  --track:#9aa0a6;
  --bg:#f1f3f5;
  --white:#ffffff;
}
*{box-sizing:border-box;margin:0;padding:0}
html,body{width:1200px;height:734px;overflow:hidden}
body{background:var(--bg);font-family:'Roboto',sans-serif;position:relative}
.screen{position:absolute;top:108px;width:218px;height:518px;background:var(--white);border-radius:10px;overflow:hidden;box-shadow:0 2px 10px rgba(0,0,0,.08)}
.screen--register{left:59px}
.screen--survey-a{left:345px}
.screen--survey-b{left:632px}
.screen--menu{left:918px}
.abs{position:absolute}
.register-wave{position:absolute;left:0;top:0}
.brand{position:absolute;top:104px;left:0;width:218px;display:flex;align-items:center;justify-content:center;gap:7px}
.brand__mark{width:12px;height:12px;background:var(--blue);border-radius:2px}
.brand__name{font-size:14px;font-weight:500;color:var(--ink);letter-spacing:1.2px}
.field{position:absolute;left:23px;width:172px;height:27px;border:1.2px solid var(--white);border-radius:14px;color:var(--white);font-size:10px;padding-left:10px;line-height:25px}
.field--submit{background:var(--white);color:var(--blue);text-align:center;padding:0}
.consent{position:absolute;top:487px;left:0;width:100%;text-align:center;color:var(--white);font-size:7.5px;line-height:10px}
.topbar{position:absolute;left:0;top:0;width:100%;height:28px;background:var(--blue)}
.burger{position:absolute;left:9px;top:8px;width:9px}
.burger span{display:block;height:1.3px;background:var(--white);margin-bottom:3px}
.pill{position:absolute;left:23px;width:172px;height:26px;border-radius:13px;background:var(--blue);color:var(--white);font-size:10px;display:flex;align-items:center;justify-content:center;gap:6px}
.rating{position:absolute;left:0;width:218px;height:44px}
.divider{position:absolute;left:0;width:100%;height:1px;background:var(--line)}
.comments-label{position:absolute;left:0;width:100%;text-align:center;font-size:9px;color:var(--muted)}
.comments-label em{font-size:6px}
.comments-box{position:absolute;left:20px;width:179px;height:83px;border:1px solid var(--line);border-radius:10px}
.drawer{position:absolute;left:0;top:0;width:173px;height:492px;background:var(--white);box-shadow:2px 0 8px rgba(0,0,0,.15)}
.drawer__profile{height:136px;background:var(--blue);position:relative}
.avatar{position:absolute;left:53px;top:32px;width:67px;height:67px;border-radius:50%;border:1.5px solid var(--white);padding:4px}
.avatar__photo{width:100%;height:100%;border-radius:50%;background:linear-gradient(#f4f6f8,#dfe3e6)}
.drawer__name{position:absolute;top:110px;width:100%;text-align:center;color:var(--white);font-size:10px}
.menu-item{height:40px;border-bottom:1px solid var(--line);text-align:center;line-height:39px;font-size:10px;color:var(--muted)}
.version{position:absolute;right:6px;bottom:4px;font-size:4.5px;color:var(--muted)}
.close{position:absolute;right:8px;top:6px}
</style>
</head>
<body>

<!-- Registration -->
<section class="screen screen--register">
  <svg class="register-wave" width="218" height="518" viewBox="0 0 218 518">
    <path d="M0 170 C10 225 70 222 110 220 C175 218 210 245 218 275 L218 518 L0 518 Z" fill="var(--blue)"/>
  </svg>
  <div class="brand"><span class="brand__mark"></span><span class="brand__name">MERIDIAN TELECOM</span></div>
  <div class="field" style="top:280px">Name</div>
  <div class="field" style="top:317px">Phone Number</div>
  <div class="field" style="top:354px">Group Number</div>
  <div class="field field--submit" style="top:391px">Register</div>
  <p class="consent">By Registering I agree to participate<br>in the Survey.</p>
</section>

<!-- Survey: call & SMS -->
<section class="screen screen--survey-a">
  <div class="topbar"><div class="burger"><span></span><span></span><span></span></div></div>
  <div class="pill" style="top:48px">
    <svg width="10" height="10" viewBox="0 0 24 24"><path d="M6.6 10.8a15 15 0 0 0 6.6 6.6l2.2-2.2a1 1 0 0 1 1-.25 11 11 0 0 0 3.6.6 1 1 0 0 1 1 1V20a1 1 0 0 1-1 1A17 17 0 0 1 3 4a1 1 0 0 1 1-1h3.5a1 1 0 0 1 1 1 11 11 0 0 0 .6 3.6 1 1 0 0 1-.25 1z" fill="#fff"/></svg>
    Call Experience</div>
  <svg class="rating" style="top:80px" viewBox="0 0 218 44">
    <g font-family="Roboto,sans-serif" font-size="9" font-weight="500" fill="#3aaee8" text-anchor="middle"><text x="23" y="11">1</text><text x="65" y="11">2</text><text x="107" y="11">3</text><text x="148" y="11">4</text><text x="189" y="11">5</text></g>
    <line x1="23" y1="26" x2="189" y2="26" stroke="#9aa0a6" stroke-width="1.3"/>
    <g fill="#9aa0a6"><circle cx="23" cy="26" r="2"/><circle cx="65" cy="26" r="2"/><circle cx="107" cy="26" r="2"/><circle cx="148" cy="26" r="2"/></g>
    <circle cx="189" cy="26" r="5.5" fill="#d4d7da" stroke="#9aa0a6"/>
    <g font-family="Roboto,sans-serif" font-size="3.8" fill="#3aaee8" text-anchor="middle"><text x="23" y="37">Somewhat</text><text x="23" y="41">Satisfied</text><text x="189" y="37">Extremely</text><text x="189" y="41">Satisfied</text></g>
  </svg>
  <div class="divider" style="top:146px"></div>
  <div class="pill" style="top:169px">
    <svg width="14" height="9" viewBox="0 0 28 18"><path d="M0 5h6M2 9h4M0 13h6" stroke="#fff" stroke-width="1.5"/><rect x="9" y="1" width="18" height="16" fill="#fff"/><path d="M9 1l9 8 9-8" stroke="#3aaee8" fill="none" stroke-width="1.5"/></svg>
    SMS Experience</div>
  <svg class="rating" style="top:201px" viewBox="0 0 218 44">
    <g font-family="Roboto,sans-serif" font-size="9" font-weight="500" fill="#3aaee8" text-anchor="middle"><text x="23" y="11">1</text><text x="65" y="11">2</text><text x="107" y="11">3</text><text x="148" y="11">4</text><text x="189" y="11">5</text></g>
    <line x1="23" y1="26" x2="189" y2="26" stroke="#9aa0a6" stroke-width="1.3"/>
    <g fill="#9aa0a6"><circle cx="23" cy="26" r="2"/><circle cx="65" cy="26" r="2"/><circle cx="107" cy="26" r="2"/><circle cx="148" cy="26" r="2"/></g>
    <circle cx="189" cy="26" r="5.5" fill="#d4d7da" stroke="#9aa0a6"/>
    <g font-family="Roboto,sans-serif" font-size="3.8" fill="#3aaee8" text-anchor="middle"><text x="23" y="37">Somewhat</text><text x="23" y="41">Satisfied</text><text x="189" y="37">Extremely</text><text x="189" y="41">Satisfied</text></g>
  </svg>
  <div class="divider" style="top:267px"></div>
  <p class="comments-label" style="top:284px">comments <em>(optional)</em></p>
  <div class="comments-box" style="top:297px"></div>
  <div class="pill" style="top:477px">Next
    <svg class="abs" style="right:8px;top:7px" width="13" height="12" viewBox="0 0 13 12"><path d="M0 6h12M7 1l5 5-5 5" stroke="#fff" stroke-width="1.2" fill="none"/></svg></div>
</section>

<!-- Survey: data & streaming -->
<section class="screen screen--survey-b">
  <div class="topbar" style="height:31px"><div class="burger" style="top:10px"><span></span><span></span><span></span></div></div>
  <div class="pill" style="top:51px">
    <svg width="11" height="10" viewBox="0 0 22 20"><rect x="0" y="0" width="22" height="5" fill="#fff"/><rect x="0" y="7.5" width="22" height="5" fill="#fff"/><rect x="0" y="15" width="22" height="5" fill="#fff"/><g fill="#3aaee8"><circle cx="18" cy="2.5" r="1"/><circle cx="18" cy="10" r="1"/><circle cx="18" cy="17.5" r="1"/></g></svg>
    Data Experience</div>
  <svg class="rating" style="top:82px" viewBox="0 0 218 44">
    <g font-family="Roboto,sans-serif" font-size="9" font-weight="500" fill="#3aaee8" text-anchor="middle"><text x="23" y="11">1</text><text x="65" y="11">2</text><text x="107" y="11">3</text><text x="148" y="11">4</text><text x="189" y="11">5</text></g>
    <line x1="23" y1="26" x2="189" y2="26" stroke="#9aa0a6" stroke-width="1.3"/>
    <g fill="#9aa0a6"><circle cx="23" cy="26" r="2"/><circle cx="65" cy="26" r="2"/><circle cx="107" cy="26" r="2"/><circle cx="148" cy="26" r="2"/></g>
    <circle cx="189" cy="26" r="5.5" fill="#d4d7da" stroke="#9aa0a6"/>
    <g font-family="Roboto,sans-serif" font-size="3.8" fill="#3aaee8" text-anchor="middle"><text x="23" y="37">Somewhat</text><text x="23" y="41">Satisfied</text><text x="189" y="37">Extremely</text><text x="189" y="41">Satisfied</text></g>
  </svg>
  <div class="divider" style="top:148px"></div>
  <div class="pill" style="top:170px">
    <svg width="16" height="9" viewBox="0 0 32 18"><rect x="1" y="1" width="30" height="16" rx="2" fill="none" stroke="#fff" stroke-width="1.6"/><path d="M13 5l7 4-7 4z" fill="#fff"/></svg>
    Streaming Experience</div>
  <svg class="rating" style="top:201px" viewBox="0 0 218 44">
    <g font-family="Roboto,sans-serif" font-size="9" font-weight="500" fill="#3aaee8" text-anchor="middle"><text x="23" y="11">1</text><text x="65" y="11">2</text><text x="107" y="11">3</text><text x="148" y="11">4</text><text x="189" y="11">5</text></g>
    <line x1="23" y1="26" x2="189" y2="26" stroke="#9aa0a6" stroke-width="1.3"/>
    <g fill="#9aa0a6"><circle cx="23" cy="26" r="2"/><circle cx="65" cy="26" r="2"/><circle cx="107" cy="26" r="2"/><circle cx="148" cy="26" r="2"/></g>
    <circle cx="189" cy="26" r="5.5" fill="#d4d7da" stroke="#9aa0a6"/>
    <g font-family="Roboto,sans-serif" font-size="3.8" fill="#3aaee8" text-anchor="middle"><text x="23" y="37">Somewhat</text><text x="23" y="41">Satisfied</text><text x="189" y="37">Extremely</text><text x="189" y="41">Satisfied</text></g>
  </svg>
  <div class="divider" style="top:267px"></div>
  <p class="comments-label" style="top:284px">comments <em>(optional)</em></p>
  <div class="comments-box" style="top:296px"></div>
  <div class="pill" style="top:474px">Send Survey</div>
</section>

<!-- Side menu open over survey -->
<section class="screen screen--menu">
  <div class="topbar"></div>
  <svg class="close" width="14" height="14" viewBox="0 0 14 14"><path d="M1 1l12 12M13 1L1 13" stroke="#fff" stroke-width="1.4"/></svg>
  <div class="pill" style="top:50px;left:23px;width:168px"></div>
  <svg class="rating" style="top:81px" viewBox="0 0 218 44">
    <text x="190" y="11" font-family="Roboto,sans-serif" font-size="9" font-weight="500" fill="#3aaee8" text-anchor="middle">5</text>
    <line x1="23" y1="26" x2="190" y2="26" stroke="#9aa0a6" stroke-width="1.3"/>
    <circle cx="190" cy="26" r="5.5" fill="#d4d7da" stroke="#9aa0a6"/>
    <g font-family="Roboto,sans-serif" font-size="3.8" fill="#3aaee8" text-anchor="middle"><text x="190" y="37">Extremely</text><text x="190" y="41">Satisfied</text></g>
  </svg>
  <div class="divider" style="top:146px"></div>
  <div class="pill" style="top:170px;left:23px;width:168px"></div>
  <svg class="rating" style="top:201px" viewBox="0 0 218 44">
    <text x="190" y="11" font-family="Roboto,sans-serif" font-size="9" font-weight="500" fill="#3aaee8" text-anchor="middle">5</text>
    <line x1="23" y1="26" x2="190" y2="26" stroke="#9aa0a6" stroke-width="1.3"/>
    <circle cx="190" cy="26" r="5.5" fill="#d4d7da" stroke="#9aa0a6"/>
    <g font-family="Roboto,sans-serif" font-size="3.8" fill="#3aaee8" text-anchor="middle"><text x="190" y="37">Extremely</text><text x="190" y="41">Satisfied</text></g>
  </svg>
  <div class="divider" style="top:267px"></div>
  <div class="comments-box" style="top:297px"></div>
  <div class="pill" style="top:477px;left:23px;width:168px"></div>

  <nav class="drawer">
    <div class="drawer__profile">
      <div class="avatar"><div class="avatar__photo" role="img" aria-label="User profile photo"></div></div>
      <p class="drawer__name">Dana Morel</p>
    </div>
    <div class="menu-item">Edit User Profile</div>
    <div class="menu-item">Survey interval Timer</div>
    <div class="menu-item">FAQ</div>
    <div class="menu-item">About</div>
    <div class="menu-item">Exit</div>
    <span class="version">1.2.1 Version</span>
  </nav>
</section>

</body>
</html>
```